Book Cover Design Project - "Cue The Panic"

"Cue the panic - making videos to boost business" is a business book that outlines what you need to know if you are planning to make videos for business communications.
The intended audience for the book is small to medium business owners. These are people who are keen to learn what they should know to do it themselves.
The cover needs to have a clear design that works as a thumbnail as well as full size.
Feel free to have some fun with it. It doesn't have to be all serious. Although this is a business book many people are afraid and don't know where to start with video production.
My company logo uses red, black, grey and white - www.velkarmedia.com.au . The logo has been uploaded.
It is not critical to use those elements, however if it can be incorporated into the design that's good too. The priority however is having a design that is eye catching.
The book will about 200 pages long. The back will include an authors photo, so blurb and testimonials- a word doc has been uploaded. It will also include the barcode, ISBN number, and price.
The spine will need to be clear and eyecatching as well.
The design should clearly reveal that this is about video production and provide a feeling of competency and comfort for those who read it.
Updates

The dimensions for the cover should be 12.8cm x 19.8cm.

At this point the spine thickness will be about 1.5cm x 19.8cm high

Please include my name on the front cover of the design:

Brent Malloway

Target Market(s)

The book is targeted to small to medium business owners who want to know how to make videos for their business. They are do it yourself people.

Industry/Entity Type

Business

Requirements
Must have
• Front
Title: Cue the panic
Tagline: Making videos to boost business

I would also like the spine and back cover done as part of the design, however let's get the front done and then the rest can be completed based on the approved design.
Nice to have
• Cue the panic is a play on words in regards to being filmed (shot) and the anxiety people feel about presenting in front of a camera.
One idea I've had (but I'm not attached to it), is to make the markings that are present in a camera's viewfinder to resemble those that are seen through the sights of a gun.
I'm really not attached to it and unless that can be achieved in a playful way, it is probably best to avoid.
Should not have
• Please avoid images of low budget cameras. The impression we want here is that this is professional standard video production advice. (By the way you don't have to have any cameras at all).

Low budget cameras are handycams etc.

```html
<!DOCTYPE html>
<html lang="en">
<head>
<meta charset="utf-8">
<title>Cue The Panic – Making Videos to Boost Business</title>
<link rel="stylesheet" href="https://fonts.googleapis.com/css2?family=Bebas+Neue&family=Arimo:wght@400;700&display=swap">
<style>
  :root {
    --cover-black: #000000;
    --lens-white: #ffffff;
    --lens-grey: #d9d9d9;
    --ink-black: #0a0a0a;
    --signal-red: #f0140c;
    --hud-white: #ffffff;
  }
  html, body {
    margin: 0;
    padding: 0;
    width: 775px;
    height: 1200px;
    overflow: hidden;
    background: var(--cover-black);
  }
  .book-cover {
    display: block;
    width: 775px;
    height: 1200px;
  }
  .title-line {
    font-family: "Bebas Neue", "Oswald", sans-serif;
    text-anchor: middle;
  }
  .title-line--dark { fill: var(--ink-black); }
  .title-line--red { fill: var(--signal-red); }
  .rec-label {
    font-family: "Arimo", Arial, sans-serif;
    font-weight: 700;
    font-size: 40px;
    fill: var(--signal-red);
    text-anchor: end;
  }
  .tagline {
    font-family: "Arimo", Arial, sans-serif;
    font-size: 29px;
    fill: var(--signal-red);
    text-anchor: middle;
  }
  .author-name {
    font-family: "Bebas Neue", "Oswald", sans-serif;
    font-size: 124px;
    fill: var(--hud-white);
    text-anchor: middle;
  }
  .crosshair-tick, .frame-corner {
    stroke-linecap: butt;
    fill: none;
  }
  .crosshair-tick { stroke: var(--ink-black); stroke-width: 3; }
  .frame-corner { stroke: var(--hud-white); stroke-width: 3; }
  .battery-outline { fill: none; stroke: var(--hud-white); stroke-width: 3; }
  .battery-cell { fill: var(--hud-white); }
</style>
</head>
<body>
<svg class="book-cover" viewBox="0 0 775 1200" xmlns="http://www.w3.org/2000/svg" role="img" aria-label="Cue The Panic – Making videos to boost business, by Brent Malloway">
  <defs>
    <radialGradient id="lens-glow" cx="50%" cy="50%" r="50%">
      <stop offset="0%" stop-color="var(--lens-white)"/>
      <stop offset="78%" stop-color="#f7f7f7"/>
      <stop offset="100%" stop-color="var(--lens-grey)"/>
    </radialGradient>
  </defs>

  <rect class="cover-background" width="775" height="1200" fill="var(--cover-black)"/>

  <!-- Viewfinder status: battery -->
  <g class="battery-indicator">
    <rect class="battery-outline" x="50" y="52" width="71" height="29" rx="2"/>
    <rect class="battery-cell" x="41" y="60" width="7" height="13"/>
    <polygon class="battery-cell" points="62,77 70,56 78,56 70,77"/>
    <polygon class="battery-cell" points="80,77 88,56 96,56 88,77"/>
    <polygon class="battery-cell" points="98,77 106,56 114,56 106,77"/>
  </g>

  <!-- Viewfinder status: recording -->
  <text class="rec-label" x="739" y="83">REC</text>

  <!-- Scope lens -->
  <circle class="scope-lens" cx="388" cy="520" r="333" fill="url(#lens-glow)"/>
  <g class="crosshair">
    <line class="crosshair-tick" x1="388" y1="187" x2="388" y2="261"/>
    <line class="crosshair-tick" x1="388" y1="784" x2="388" y2="853"/>
    <line class="crosshair-tick" x1="55" y1="522" x2="128" y2="522"/>
    <line class="crosshair-tick" x1="647" y1="522" x2="720" y2="522"/>
  </g>

  <!-- Title -->
  <text class="title-line title-line--dark" x="388" y="368" font-size="116">CUE</text>
  <text class="title-line title-line--dark" x="388" y="581" font-size="268">THE</text>
  <text class="title-line title-line--red" x="388" y="762" font-size="196">PANIC</text>

  <!-- Tagline frame -->
  <g class="tagline-frame">
    <polyline class="frame-corner" points="57,942 57,921 79,921"/>
    <polyline class="frame-corner" points="698,921 720,921 720,942"/>
    <polyline class="frame-corner" points="57,1003 57,1025 79,1025"/>
    <polyline class="frame-corner" points="698,1025 720,1025 720,1003"/>
  </g>
  <text class="tagline" x="388" y="984" textLength="626" lengthAdjust="spacing">MAKING VIDEOS TO BOOST BUSINESS</text>

  <!-- Author -->
  <text class="author-name" x="388" y="1155" textLength="522" lengthAdjust="spacingAndGlyphs">BRENT MALLOWAY</text>
</svg>
</body>
</html>
```